Awesome business card design needed

We need a new business card design to go with our new logo.
We are a web development agency that specialises in highly complex back-end integrations as opposed to design, our customers are retailers, hotels, hospitals and any other organisation that has a large online marketing department.
Take a look at our website - www.orvekplus.com for some inspiration.
We want our new business cards to exude class, professionalism and style.
We are likely to choose a high-end card to print them on but we want the design of the card itself to really turn heads.
We have no specific colour requirements, the logo as you will see is a turquoise colour R89 G171 B167 #59aba7 but it can also be in white if you want to make the colour of the card something different.
The information on the card should be:
Name
Position
Tel
email
Potentially a double sided card could have our web address, twitter and FB links.

```html
<!DOCTYPE html>
<html lang="en">
<head>
<meta charset="utf-8">
<title>orvekplus business cards</title>
<link rel="stylesheet" href="https://fonts.googleapis.com/css2?family=Exo+2:wght@300;400;600&family=Rajdhani:wght@600&display=swap">
<style>
  :root {
    --turquoise: #59aba7;
    --teal-card: #4f7f83;
    --band-dark: #2b2f31;
    --paper: #f7f7f5;
    --ink: #4a4a4a;
    --ink-soft: #7a7a7a;
    --stage: #e6e6e4;
    --city-deep: #1d3350;
    --city-light: #4f7196;
  }
  * { margin: 0; padding: 0; box-sizing: border-box; }
  html, body { width: 1200px; height: 868px; overflow: hidden; }
  body {
    background: var(--stage);
    font-family: "Exo 2", sans-serif;
    position: relative;
  }
  .card {
    position: absolute;
    top: 284px;
    width: 520px;
    height: 300px;
    overflow: hidden;
    box-shadow: 0 2px 10px rgba(0,0,0,0.12);
  }
  /* Front */
  .card--front { left: 53px; background: var(--paper); }
  .front__logo {
    position: absolute;
    left: 28px;
    top: 22px;
    font-family: "Exo 2", sans-serif;
    font-weight: 600;
    font-size: 62px;
    letter-spacing: 2px;
    color: var(--turquoise);
    line-height: 1;
  }
  .front__block {
    position: absolute;
    left: 0;
    bottom: 40px;
  }
  .front__avatar {
    position: absolute;
    left: 10px;
    bottom: 40px;
    width: 90px;
    height: 96px;
    background: linear-gradient(180deg, #b98a6e, #6b4a3a 70%, #8c1f24);
  }
  .front__city {
    position: absolute;
    left: 0;
    right: 0;
    bottom: 0;
    height: 40px;
    background: linear-gradient(90deg, var(--city-deep), var(--city-light) 40%, var(--city-deep) 70%, #3a5676);
  }
  .front__person {
    position: absolute;
    left: 262px;
    top: 150px;
  }
  .person__name {
    font-weight: 400;
    font-size: 22px;
    color: var(--ink);
  }
  .person__role {
    font-weight: 300;
    font-size: 12px;
    color: var(--ink-soft);
    margin-top: 2px;
  }
  /* Back */
  .card--back { left: 627px; background: var(--teal-card); }
  .back__logo {
    position: absolute;
    left: 0;
    right: 0;
    top: 86px;
    text-align: center;
    font-family: "Exo 2", sans-serif;
    font-weight: 600;
    font-size: 66px;
    letter-spacing: 2px;
    color: var(--turquoise);
    line-height: 1;
  }
  .back__email {
    position: absolute;
    left: 22px;
    bottom: 44px;
    font-family: "Rajdhani", sans-serif;
    font-weight: 600;
    font-size: 13px;
    letter-spacing: 1px;
    color: var(--turquoise);
  }
  .back__band {
    position: absolute;
    left: 0;
    right: 0;
    bottom: 0;
    height: 38px;
    background: var(--band-dark);
    display: flex;
    align-items: center;
    padding-left: 22px;
    font-family: "Rajdhani", sans-serif;
    font-weight: 600;
    font-size: 13px;
    letter-spacing: 1px;
    color: #e9ecec;
    text-transform: uppercase;
  }
</style>
</head>
<body>
  <section class="card card--front">
    <svg class="front__block" width="240" height="180" viewBox="0 0 240 180">
      <path d="M0 0 H110 V60 H240 V180 H0 Z" fill="var(--turquoise)"/>
    </svg>
    <div class="front__logo">orvekplus</div>
    <div class="front__avatar" role="img" aria-label="Cartoon portrait of the cardholder"></div>
    <div class="front__person">
      <p class="person__name">Owen Marsh</p>
      <p class="person__role">Co-Founder and incredible coder</p>
    </div>
    <div class="front__city" role="img" aria-label="Night-time photo of an office building facade"></div>
  </section>

  <section class="card card--back">
    <div class="back__logo">orvekplus</div>
    <p class="back__email">info@orvekplus.com // 01632 960418</p>
    <div class="back__band">orvekplus Ltd, Harwick House, 12 Mill Lane, Ashbourne, AB1 2CD</div>
  </section>
</body>
</html>
```